Web Design Project

I want customers to be able to book appointments to get their makeup done and make a deposit and also have a gallery where i put my portfolio images, i want it to be very simple yet elegant.

Target Market(s)

Women ranging from 18-40 that want to get their makeup done

Industry/Entity Type

Makeup

Font styles to use
Sans Serif
Decorative

Requirements
Nice to have
• easy scheduling option and option to pay service in full on website.

```html
<!DOCTYPE html>
<html lang="en">
<head>
<meta charset="utf-8">
<title>Clara Voss Makeup – Book Online</title>
<link href="https://fonts.googleapis.com/css2?family=Questrial&family=Arimo:wght@400;700&family=Josefin+Sans:wght@300&display=swap" rel="stylesheet">
<style>
:root{
  --ink:#1c1c1c;
  --footer:#1b1b1b;
  --bar:#242424;
  --white:#ffffff;
  --red:#b3161b;
  --btn:#a30f13;
  --text:#333333;
  --muted:#888888;
  --rule:#dddddd;
  --panel:#efefef;
  --panel-head:#dcdcdc;
  --foot-text:#d6d6d6;
  --icon:#6a6a6a;
}
*{margin:0;padding:0;box-sizing:border-box}
html,body{width:1200px;height:809px;overflow:hidden;background:var(--white)}
body{position:relative;font-family:"Questrial",sans-serif;color:var(--text)}
.abs{position:absolute}

/* header */
.site-header{position:absolute;left:0;top:0;width:1200px;height:113px;background:var(--ink)}
.brand{position:absolute;left:240px;top:30px;font-family:"Josefin Sans",sans-serif;font-weight:300;font-size:40px;letter-spacing:2px;color:var(--white);line-height:48px}
.nav-item{position:absolute;top:47px;text-align:center;width:110px;margin-left:-55px}
.nav-item .label{display:block;font-size:12px;color:var(--white);letter-spacing:.3px}
.nav-item .sub{display:block;font-family:"Arimo",sans-serif;font-size:9px;color:#cfcfcf;margin-top:8px}
.nav-item.active .label{color:var(--red)}
.nav-sep{position:absolute;top:48px;width:1px;height:34px;background:#6a6a6a}

/* photo strip */
.gallery-strip{position:absolute;left:0;top:113px;width:1200px;height:172px;background:#262626}
.shot{position:absolute;top:0;width:120px;height:158px}

/* content */
.page-title{position:absolute;left:240px;top:303px;font-size:15px;letter-spacing:.8px;color:var(--red)}
.services{position:absolute;left:240px;top:346px;width:491px}
.services-head{height:21px;font-size:11px;color:var(--muted);letter-spacing:.4px;border-bottom:1px solid var(--rule)}
.service{position:relative;border-bottom:1px solid var(--rule);font-size:12px;letter-spacing:.3px}
.service .name{position:absolute;left:0;top:16px}
.service .note{position:absolute;left:0;top:34px;font-family:"Arimo",sans-serif;font-style:italic;font-size:10px;color:var(--muted);line-height:12px}
.service .price{position:absolute;left:238px;width:60px;top:16px;text-align:center}
.service .time{position:absolute;left:334px;width:60px;top:16px;text-align:center}
.request{position:absolute;left:424px;top:12px;width:51px;height:20px;background:var(--btn);color:var(--white);font-family:"Arimo",sans-serif;font-size:10px;line-height:20px;text-align:center;border-radius:2px}

.help-panel{position:absolute;left:748px;top:332px;width:215px;height:270px;background:var(--panel);font-family:"Arimo",sans-serif}
.panel-head{height:28px;background:var(--panel-head);font-size:10px;font-weight:700;color:#222;line-height:28px;padding-left:23px;position:relative}
.panel-head svg{position:absolute;left:6px;top:8px}
.help-list{list-style:none;padding:8px 0 4px 4px}
.help-list li{font-size:9px;color:#555;height:23px;line-height:16px}
.help-list li span{color:#bbb;margin-right:5px}
.panel-text{font-size:8.5px;color:#666;padding:16px 4px 0 3px;line-height:11px}
.panel-text a{color:#222;text-decoration:none}

/* footer */
.site-footer{position:absolute;left:0;top:643px;width:1200px;height:134px;background:var(--footer);font-family:"Arimo",sans-serif;color:var(--foot-text)}
.hours{position:absolute;left:269px;top:20px;font-size:10px;line-height:16px}
.hours td{padding-right:4px}
.card-badge{position:absolute;top:90px;width:30px;height:19px;border-radius:2px}
.address{position:absolute;left:531px;top:17px;font-size:10px;line-height:16px}
.phone{position:absolute;left:531px;top:74px;font-size:14px}
.social{position:absolute;top:23px;width:23px;height:23px;background:var(--white)}
.store{position:absolute;top:65px;width:76px;height:24px;background:#0f0f0f;border:1px solid #333;border-radius:3px}
.copyright{position:absolute;left:0;top:777px;width:1200px;height:32px;background:var(--bar);font-family:"Arimo",sans-serif;font-size:9.5px;color:#aaa;text-align:center;line-height:36px}
</style>
</head>
<body>

<header class="site-header">
  <div class="brand">CLARA VOSS</div>
  <nav>
    <div class="nav-item" style="left:537px"><span class="label">HOME</span><span class="sub">home page</span></div>
    <div class="nav-sep" style="left:576px"></div>
    <div class="nav-item" style="left:617px"><span class="label">ABOUT US</span><span class="sub">Clara Voss</span></div>
    <div class="nav-sep" style="left:669px"></div>
    <div class="nav-item" style="left:719px"><span class="label">PORTFOLIO</span><span class="sub">my work</span></div>
    <div class="nav-sep" style="left:763px"></div>
    <div class="nav-item" style="left:812px"><span class="label">TESTIMONIALS</span><span class="sub">what client say</span></div>
    <div class="nav-sep" style="left:870px"></div>
    <div class="nav-item active" style="left:923px"><span class="label">BOOK ONLINE</span><span class="sub">book appoiment</span></div>
  </nav>
</header>

<section class="gallery-strip">
  <div class="shot" style="left:0;background:linear-gradient(135deg,#2a2320,#8a6a58 60%,#1a1512)" role="img" aria-label="Portfolio photo: makeup portrait"></div>
  <div class="shot" style="left:120px;background:linear-gradient(180deg,#b9b2ae,#9c7f70 55%,#e8e4e2)" role="img" aria-label="Portfolio photo: makeup portrait"></div>
  <div class="shot" style="left:240px;background:linear-gradient(135deg,#4a3a30,#a58066 55%,#3a2c24)" role="img" aria-label="Portfolio photo: makeup portrait"></div>
  <div class="shot" style="left:360px;background:linear-gradient(135deg,#cfc6c8,#8f6a6c 50%,#2c2222)" role="img" aria-label="Portfolio photo: makeup portrait"></div>
  <div class="shot" style="left:480px;background:linear-gradient(135deg,#a87a5a,#d6b59c 55%,#6a4a36)" role="img" aria-label="Portfolio photo: makeup portrait"></div>
  <div class="shot" style="left:600px;background:linear-gradient(135deg,#2a2a2e,#b58a78 55%,#3a2a26)" role="img" aria-label="Portfolio photo: makeup portrait"></div>
  <div class="shot" style="left:720px;background:linear-gradient(135deg,#151515,#c2a596 55%,#1c1a1a)" role="img" aria-label="Portfolio photo: makeup portrait"></div>
  <div class="shot" style="left:840px;background:linear-gradient(135deg,#1f2430,#b8a0a0 55%,#2a2628)" role="img" aria-label="Portfolio photo: makeup portrait"></div>
  <div class="shot" style="left:960px;background:linear-gradient(135deg,#3a2a24,#c6a090 55%,#2a1e1a)" role="img" aria-label="Portfolio photo: makeup portrait"></div>
  <div class="shot" style="left:1080px;background:linear-gradient(135deg,#c7b7ae,#b08e7a 55%,#2a2220)" role="img" aria-label="Portfolio photo: makeup portrait"></div>
</section>

<main>
  <h1 class="page-title">BOOK APPOINTMENT ONLINE</h1>

  <div class="services">
    <div class="services-head">MY SERVICES</div>
    <div class="service" style="height:45px">
      <span class="name">Just want your makeup done</span>
      <span class="price">$25</span><span class="time">30 min.</span>
      <span class="request">Request</span>
    </div>
    <div class="service" style="height:69px">
      <span class="name">Private Class</span>
      <span class="note">Learn the basics to makeup with a little<br>one-on-one time with us at Studio Rouge</span>
      <span class="price">$100</span><span class="time">2 hr.</span>
      <span class="request">Request</span>
    </div>
    <div class="service" style="height:46px">
      <span class="name">Prom</span>
      <span class="price">$40</span><span class="time">1 hr.</span>
      <span class="request">Request</span>
    </div>
    <div class="service" style="height:57px">
      <span class="name">Weddings</span>
      <span class="note">50$ a person</span>
      <span class="price">$50</span><span class="time">2 hr.</span>
      <span class="request">Request</span>
    </div>
  </div>

  <aside class="help-panel">
    <div class="panel-head">
      <svg width="11" height="13" viewBox="0 0 11 13"><text x="1" y="11" font-family="Arimo,sans-serif" font-weight="700" font-size="13" fill="#888">?</text></svg>
      How Do I...
    </div>
    <ul class="help-list">
      <li><span>?</span>View a previous booking?</li>
      <li><span>?</span>Reserve multiple services?</li>
      <li><span>?</span>View descriptions of services or packages?</li>
    </ul>
    <div class="panel-head">
      <svg width="12" height="13" viewBox="0 0 12 13"><circle cx="6" cy="4" r="3" fill="#888"/><path d="M0 13c0-4 3-5 6-5s6 1 6 5z" fill="#888"/></svg>
      My Appointments
    </div>
    <p class="panel-text">View upcoming appointments or quickly re-book past appointments.<br><br>If you've already booked with us, <a>Log in »</a></p>
  </aside>
</main>

<footer class="site-footer">
  <svg class="abs" style="left:239px;top:20px" width="17" height="17" viewBox="0 0 17 17"><circle cx="8.5" cy="8.5" r="7.5" fill="none" stroke="var(--icon)" stroke-width="1.5"/><path d="M8.5 4v5h3" fill="none" stroke="var(--icon)" stroke-width="1.5"/></svg>
  <table class="hours">
    <tr><td>Mon - Fri</td><td>: 9:00am to 7:00pm</td></tr>
    <tr><td>Sat</td><td>: 8:00am to 4:00pm</td></tr>
    <tr><td>Sun</td><td>: Closed</td></tr>
  </table>
  <svg class="abs" style="left:240px;top:91px" width="17" height="12" viewBox="0 0 17 12"><rect x=".5" y=".5" width="16" height="11" rx="1" fill="none" stroke="var(--icon)"/><rect x="0" y="3" width="17" height="2" fill="var(--icon)"/></svg>
  <div class="card-badge" style="left:271px;background:#e9e9ee"></div>
  <div class="card-badge" style="left:303px;background:#3a6fb0"></div>
  <div class="card-badge" style="left:335px;background:#e87a2a"></div>

  <svg class="abs" style="left:504px;top:19px" width="11" height="17" viewBox="0 0 11 17"><path d="M5.5 0A5.5 5.5 0 0 0 0 5.5C0 10 5.5 17 5.5 17S11 10 11 5.5A5.5 5.5 0 0 0 5.5 0z" fill="var(--icon)"/><circle cx="5.5" cy="5.5" r="2" fill="var(--footer)"/></svg>
  <p class="address">Lorem ipsum dolor sit amet, consec-<br>tetuer adipiscing elit, sed diam,<br>nonummy nibh euismod tincidunt</p>
  <svg class="abs" style="left:501px;top:76px" width="18" height="12" viewBox="0 0 18 12"><path d="M1 4c0-3 16-3 16 0v2h-4V4H5v2H1z" fill="var(--icon)"/><rect x="4" y="6" width="10" height="6" rx="1" fill="var(--icon)"/></svg>
  <div class="phone">0198 765 432</div>

  <div class="social" style="left:798px" role="img" aria-label="Social link"></div>
  <div class="social" style="left:826px" role="img" aria-label="Social link"></div>
  <div class="social" style="left:854px" role="img" aria-label="Social link"></div>
  <div class="social" style="left:882px" role="img" aria-label="Social link"></div>
  <div class="social" style="left:910px" role="img" aria-label="Social link"></div>
  <div class="social" style="left:938px" role="img" aria-label="Social link"></div>

  <div class="store" style="left:802px" role="img" aria-label="App download badge"></div>
  <div class="store" style="left:882px" role="img" aria-label="App download badge"></div>
</footer>
<div class="copyright">Copyright © 2014 by Clara Voss. All rights reserved.</div>

</body>
</html>
```